Template design for an Online "Membership Subscription" System

I need a template for a service that will allow website owners to create their own online subscription services and member portals.
With just a snippet of code they can password protect certain parts of their website.
Tagline:
"Monetize your website with TallyGateClubs"
"The Easiest Way To Turn Your Website Into 'Members Only'"
Call to action "Try For Free" and "Watch a demo"
Features:
1. Quick & easy to set up
2. Works with any website
3. Charge one-time or subscription fees
4. Automated billing, sign up and more
5. Customize to match your website
6. Unlimited members
Similar websites/services;
https://lockvaultsuite.example
https://joinrova.example
https://www.guildnook.example
I'd like a clean looking, uncluttered design targeted towards "non-techie" people. Easy to read without a lot going on. Emphasizing ease of use and pushing towards a "Try for free" option.
Separate into sections with the top section having the tagline. Followed by feature overview, testimonials, sample use cases.
A footer with multiple links by industry that can provide a case study for various use cases;
Ex;
Clubs
Religious Organizations
Online Stores
Digital Products
Education
Coaching
Fitness
Target Market(s)
Non technical small business owners
Number of Pages Required
2 page
Look and feel
Each slider illustrates characteristics of the customer's brand and the style your logo design should communicate.

```html
<!DOCTYPE html>
<html lang="en">
<head>
<meta charset="utf-8">
<title>TallyGateClubs – Membership Subscriptions</title>
<link href="https://fonts.googleapis.com/css2?family=IBM+Plex+Sans:ital,wght@0,400;0,500;0,600;0,700;1,400&family=Poppins:wght@400;700&family=Roboto:wght@400;500;700&display=swap" rel="stylesheet">
<style>
:root{
  --cyan:#0a9fdc;
  --navy:#0d4fa9;
  --ink:#1f1f24;
  --body:#55585f;
  --band:#e3f2fa;
  --band-deep:#d6ecf7;
  --line:#c9dde8;
  --white:#ffffff;
}
*{box-sizing:border-box;margin:0;padding:0}
html,body{width:1200px;height:3095px;overflow:hidden;background:var(--white)}
body{position:relative;font-family:"IBM Plex Sans",sans-serif;color:var(--ink)}
.abs{position:absolute}
.topbar{left:0;top:0;width:1200px;height:8px;background:var(--cyan)}
.brand{left:117px;top:30px;display:flex;align-items:center;gap:10px;font:700 27px "IBM Plex Sans",sans-serif;color:var(--navy)}
.brand-dot{width:26px;height:26px;border-radius:50%;background:var(--cyan)}
.nav{left:402px;top:40px;font:400 15px "Roboto",sans-serif;color:#333}
.nav a{position:absolute;white-space:nowrap;color:inherit;text-decoration:none}
.nav .active{color:var(--cyan);border-bottom:2px solid var(--cyan);padding-bottom:3px}
.btn{display:flex;align-items:center;justify-content:center;font:700 14px "Roboto",sans-serif;color:var(--white);text-transform:uppercase}
.get-started{left:913px;top:28px;width:142px;height:42px;background:var(--cyan);border-radius:3px;gap:10px}
.hero-title{left:142px;top:202px;font:700 54px/60px "IBM Plex Sans",sans-serif;color:var(--ink)}
.hero-sub{left:142px;top:413px;font:500 18px "IBM Plex Sans",sans-serif;color:#2b2b30}
.pill{height:41px;border-radius:21px}
.try{left:142px;top:477px;width:143px;background:var(--navy)}
.demo{left:291px;top:477px;width:143px;background:var(--cyan)}
.hero-art{left:672px;top:216px;width:511px;height:330px;border-radius:20px;background:linear-gradient(135deg,#dcecf8,#c4d8f2 55%,#f2e0b8)}
.dots{left:575px;top:570px;display:flex;gap:10px}
.dots i{width:10px;height:10px;border-radius:50%;background:#b9c3d3}
.dots i.on{background:var(--navy)}
.section-title{left:0;width:1200px;text-align:center;font:700 53px "IBM Plex Sans",sans-serif;color:var(--ink)}
.feat-head{left:144px;top:926px;font:600 26px "IBM Plex Sans",sans-serif}
.feat-text{left:145px;top:978px;width:396px;font:400 15.5px/23.5px "IBM Plex Sans",sans-serif;color:var(--body);text-align:justify}
.feat-art{left:112px;top:1066px;width:446px;height:303px;border-radius:24px;background:linear-gradient(135deg,#c9dcf5,#eaf3fb 50%,#f6d0d4)}
.feat-list{left:610px;top:925px;width:465px;list-style:none}
.feat-list li{height:64.5px;display:flex;align-items:center;gap:22px;border-bottom:1px solid var(--line);font:500 19.5px "IBM Plex Sans",sans-serif;color:#222}
.feat-list li.current{color:var(--navy)}
.feat-list svg{width:44px;height:44px;flex:none;stroke:#222;fill:none;stroke-width:1.6}
.feat-list li.current svg{stroke:var(--navy)}
.review{width:470px;height:120px}
.avatar{left:0;top:0;width:113px;height:113px;border-radius:50%;background:linear-gradient(160deg,#d9d4cc,#b08a70);border:2px solid #cfe5ee}
.quote{left:132px;top:10px;width:310px;font:italic 400 12.8px/22.5px "IBM Plex Sans",sans-serif;color:#3b3d42}
.author{left:132px;top:103px;font:600 14.5px "IBM Plex Sans",sans-serif;color:var(--navy)}
.qmark{left:405px;top:72px;font:700 60px/1 "Poppins",sans-serif;color:var(--cyan)}
.more{left:470px;top:1976px;width:260px;height:40px;border-radius:20px;background:var(--cyan);font-size:13px}
.uses-text{left:200px;top:2285px;width:800px;text-align:center;font:400 14px/29px "Poppins",sans-serif;color:#444}
.case{top:2372px;width:210px;height:249px;border-radius:10px;display:flex;align-items:flex-end;justify-content:center;padding-bottom:18px;text-align:center;font:700 25px/28px "Poppins",sans-serif;color:var(--white)}
.case-clubs{left:144px;background:linear-gradient(160deg,#1b3f7a,#0b1a33 60%,#6b4a2a)}
.case-religious{left:378px;background:linear-gradient(160deg,#d9d2c6,#8faab5 55%,#6b5a4b)}
.case-stores{left:613px;background:linear-gradient(160deg,#c99a6a,#7a5a3a 55%,#3a2a1f)}
.case-digital{left:847px;background:linear-gradient(160deg,#2a2c2f,#5a5d60 50%,#1a1b1d)}
.chev{width:20px;height:34px;stroke:#666;stroke-width:2;fill:none}
.footer{left:0;top:2717px;width:1200px;height:378px;background:var(--navy);color:var(--white)}
.foot-head{top:80px;font:600 25px "IBM Plex Sans",sans-serif}
.foot-links{top:126px;list-style:none;font:400 14.5px/29px "IBM Plex Sans",sans-serif}
.news-text{left:584px;top:126px;font:400 14.5px/29px "IBM Plex Sans",sans-serif}
.email{left:585px;top:172px;width:295px;height:40px;border-radius:20px;background:var(--white);color:#333;font:400 13px "Roboto",sans-serif;padding:13px 0 0 33px}
.signup{left:886px;top:172px;width:143px;height:40px;border-radius:20px;background:var(--cyan);font-size:14px}
.foot-rule{left:0;top:271px;width:1200px;height:1px;background:rgba(255,255,255,.12)}
.socials{left:157px;top:318px;display:flex;gap:5px}
.socials i{width:21px;height:21px;border-radius:50%;border:1.3px solid var(--white)}
.legal{left:389px;top:320px;font:400 12.5px "Roboto",sans-serif;white-space:nowrap}
</style>
</head>
<body>
<div class="abs topbar"></div>

<header>
  <div class="abs brand"><span class="brand-dot"></span>TallyGateClubs</div>
  <nav class="abs nav">
    <a class="active" style="left:0">HOME</a>
    <a style="left:62px">ABOUT US</a>
    <a style="left:154px">FEATURES</a>
    <a style="left:247px">TESTIMONIALS</a>
    <a style="left:372px">CONTACT US</a>
  </nav>
  <a class="abs btn get-started">Get Started
    <svg width="14" height="14" viewBox="0 0 14 14"><circle cx="7" cy="7" r="6.5" fill="#fff"/><path d="M4 7h5M7 4.5L9.5 7 7 9.5" stroke="#0a9fdc" stroke-width="1.8" fill="none"/></svg>
  </a>
</header>

<section class="hero">
  <h1 class="abs hero-title">Monetize your<br>Website with<br>TallyGateClubs</h1>
  <p class="abs hero-sub">The Easiest Way To Turn Your Website Into 'Members Only</p>
  <a class="abs btn pill try">Try For Free</a>
  <a class="abs btn pill demo">Watch a Demo</a>
  <div class="abs hero-art" role="img" aria-label="Illustration of a laptop showing a members-only website with a person announcing through a megaphone"></div>
  <div class="abs dots"><i></i><i class="on"></i><i></i></div>
</section>

<svg class="abs" style="left:0;top:0;width:1200px;height:1600px" viewBox="0 0 1200 1600" aria-hidden="true">
  <path d="M0,700 C150,640 280,640 430,665 C600,695 720,640 880,650 C1010,658 1110,690 1200,675 L1200,1480 C1080,1520 960,1545 820,1530 C660,1515 520,1550 360,1525 C220,1505 110,1470 0,1495Z" fill="#e3f2fa"/>
  <path d="M450,655 C600,620 720,660 860,690 C760,720 620,735 500,705Z" fill="#d6ecf7"/>
  <path d="M80,1470 C240,1430 400,1445 560,1480 C420,1515 240,1520 80,1470Z" fill="#d6ecf7"/>
</svg>

<section class="features">
  <h2 class="abs section-title" style="top:786px">Our Features</h2>
  <h3 class="abs feat-head">Quick &amp; easy to set up</h3>
  <p class="abs feat-text">Lorem ipsum dolor sit amet, consectetur adipiscing elit, sed do eiusmod tempor incididunt ut labore et dolore magnsum suspendisse ultrices gravisus</p>
  <div class="abs feat-art" role="img" aria-label="Illustration of people reviewing analytics dashboards and a mobile screen"></div>
  <ul class="abs feat-list">
    <li class="current"><svg viewBox="0 0 44 44"><circle cx="25" cy="25" r="14"/><path d="M25 16v9l6 4M21 9h8M3 22h8M5 28h6M7 34h8"/></svg>Quick &amp; easy to set up</li>
    <li><svg viewBox="0 0 44 44"><circle cx="22" cy="22" r="18"/><path d="M4 22h36M22 4c-8 8-8 28 0 36M22 4c8 8 8 28 0 36"/></svg>Works with any website</li>
    <li><svg viewBox="0 0 44 44"><rect x="5" y="4" width="34" height="26" rx="2"/><path d="M11 11h22M11 17h22M11 23h14M20 44V30l5 4"/></svg>Charge one-time or subscription fees</li>
    <li><svg viewBox="0 0 44 44"><circle cx="22" cy="22" r="12"/><path d="M18 16l9 6-9 6z"/><path d="M4 4h6M34 4h6M4 40h6M34 40h6M4 4v6M40 4v6M4 34v6M40 34v6"/></svg>Automated billing, sign up and more</li>
    <li><svg viewBox="0 0 44 44"><rect x="4" y="6" width="36" height="32" rx="2"/><path d="M4 13h36"/><circle cx="22" cy="26" r="5"/><circle cx="22" cy="26" r="9" stroke-dasharray="3 3"/></svg>Customize to match your website</li>
    <li><svg viewBox="0 0 44 44"><circle cx="22" cy="16" r="5"/><circle cx="10" cy="24" r="4"/><circle cx="34" cy="24" r="4"/><path d="M14 40v-8a8 8 0 0116 0v8M2 40v-6a8 8 0 0112-4M42 40v-6a8 8 0 00-12-4"/></svg>Unlimited members</li>
  </ul>
</section>

<section class="testimonials">
  <h2 class="abs section-title" style="top:1653px">Customer Testimonials</h2>
  <article class="abs review" style="left:132px;top:1782px">
    <div class="abs avatar" role="img" aria-label="Customer portrait"></div>
    <p class="abs quote">Sed ut perspiciatis unde omnis iste natus error sit voluptatem accusantium doloremque laudantium, totam rem aperiam, eaque ipsa quae ab illo inventore veritatis et quasi architecto beatae vitae</p>
    <p class="abs author">Dana Whitlow - TallyGateClubs</p>
    <span class="abs qmark">”</span>
  </article>
  <article class="abs review" style="left:631px;top:1782px">
    <div class="abs avatar" role="img" aria-label="Customer portrait"></div>
    <p class="abs quote">Sed ut perspiciatis unde omnis iste natus error sit voluptatem accusantium doloremque laudantium, totam rem aperiam, eaque ipsa quae ab illo inventore veritatis et quasi architecto beatae vitae</p>
    <p class="abs author">Dana Whitlow - TallyGateClubs</p>
    <span class="abs qmark" style="left:395px">”</span>
  </article>
  <a class="abs btn more">Read More Testimonials</a>
</section>

<section class="uses">
  <h2 class="abs section-title" style="top:2205px">Sample Use Cases</h2>
  <p class="abs uses-text">Sed ut perspiciatis unde omnis iste natus error sit &nbsp;voluptatem accusantium doloremque laudantium, totam rem aperiam, eaque ipsa quae ab illo inventore veritatis et quasi architecto beatae.</p>
  <svg class="abs chev" style="left:113px;top:2480px" viewBox="0 0 20 34"><path d="M17 2L3 17l14 15"/></svg>
  <div class="abs case case-clubs" role="img" aria-label="Photo of a gamer at a computer, representing clubs">Clubs</div>
  <div class="abs case case-religious" role="img" aria-label="Photo of a tablet showing a church, representing religious organizations">Religious<br>Organizations</div>
  <div class="abs case case-stores" role="img" aria-label="Photo of two women shopping online, representing online stores">Online Stores</div>
  <div class="abs case case-digital" role="img" aria-label="Photo of a laptop announcing a new product, representing digital products">Digital<br>Products</div>
  <svg class="abs chev" style="left:1066px;top:2480px" viewBox="0 0 20 34"><path d="M3 2l14 15L3 32"/></svg>
</section>

<footer class="abs footer">
  <h4 class="abs foot-head" style="left:168px">Case Studies</h4>
  <ul class="abs foot-links" style="left:168px"><li>Clubs</li><li>Religious Organizations</li><li>Online Stores</li><li>Digital Products</li></ul>
  <ul class="abs foot-links" style="left:377px"><li>Education</li><li>Coaching</li><li>Fitness</li></ul>
  <h4 class="abs foot-head" style="left:584px">Sign Up Newsletter</h4>
  <p class="abs news-text">Lorem ipsum dolor sit amet, consectetur adipiscing elit</p>
  <div class="abs email">Enter Email</div>
  <a class="abs btn signup">Sign Up</a>
  <div class="abs foot-rule"></div>
  <div class="abs socials"><i></i><i></i><i></i><i></i></div>
  <p class="abs legal">Copyrights © 2022, TallyGateClubs.All rights reserved &nbsp;| &nbsp;Privacy policy &nbsp;| &nbsp;Site Map &nbsp;| &nbsp;Disclaimer &nbsp;| &nbsp;Terms of use</p>
</footer>
</body>
</html>
```